Life Coach business needs a website design

I would like to get support in creating a website design. I will be starting a business as a life coach and I would like to start with something basic, but chic. It will be mainly a blog for now, but then I would like to start adding videos and hopefully podcast in the future. I took professional pictures of myself that I would like to include as a cover page. My main goal with this website is to capture the right audience by connecting with them through my mission, which is to embrace their inner greatness. I want to provide a sense of love, courage and authenticity when they open my website. I have a domain in Pagewell called :"Unfold the hidden bloom". I would be happy to discuss more of the details over the phone.

Target Market(s)

Young Adults (25-35)

Number of Pages Required

4 page

Colors

Designer to choose colors to be used in the design.

Requirements
Must have
• I am looking for a similar layout and vibe to these websites: https://tessawhorlby.com/meet-tessa/
• https://www.junopraskett.com
• My home page will include: About, Blog, Podcast, Subscribe.. (We can add icons of snapverra, clipvane and Boardlyn)
• I would like to have my name in the middle (Lunet), and include a note next to my picture "Your life is like a blank canvas and only you have the power to transform it into masterpiece. Take a chance and unfold the hidden bloom" L.T.

```html
<!DOCTYPE html>
<html lang="en">
<head>
<meta charset="utf-8">
<title>Unfold the hidden bloom — Lunet, Life Coach</title>
<link href="https://fonts.googleapis.com/css2?family=Montserrat:ital,wght@0,300;0,400;0,500;0,600;0,700;1,300;1,400&family=Great+Vibes&display=swap" rel="stylesheet">
<style>
:root{
  --pink:#e38b87;
  --pink-soft:#f4c9c6;
  --teal:#68a9b4;
  --teal-light:#b3d5dc;
  --teal-text:#5fa6b2;
  --ink:#2e2e2e;
  --grey:#8a8a8a;
  --blush:#fdf3f1;
  --mist:#eef8fb;
  --white:#ffffff;
}
*{box-sizing:border-box;margin:0;padding:0}
html,body{width:1200px;height:3750px;overflow:hidden}
body{font-family:'Montserrat',sans-serif;color:var(--ink);background:var(--white);position:relative}
.abs{position:absolute}
a{color:inherit;text-decoration:none}

/* nav */
.topnav{top:0;left:0;width:1200px;height:54px;background:var(--white)}
.topnav .links{left:169px;top:0;height:54px}
.topnav .links a{position:absolute;top:24px;font-size:10px;letter-spacing:.3px;text-transform:uppercase;white-space:nowrap}
.topnav .active::after{content:"";position:absolute;left:0;right:0;top:25px;height:3px;background:var(--pink)}
.social{display:flex;gap:8px;font-size:9px;color:var(--teal);font-weight:500}

/* hero */
.hero{top:54px;left:0;width:1200px;height:569px}
.hero-photo{left:0;top:0;width:1200px;height:569px;background:linear-gradient(180deg,#5aa3b6 0%,#86b3bd 55%,#b09a7c 100%)}
.hero h1{left:173px;top:195px;font-size:35px;font-weight:700;color:var(--white);letter-spacing:.3px}
.hero p{left:173px;top:253px;font-size:25px;font-weight:300;color:var(--white);line-height:36px}
.btn-pink{background:var(--pink);color:var(--white);border-radius:20px;font-size:10px;font-weight:700;
  display:flex;align-items:center;justify-content:center;gap:12px;letter-spacing:.4px}
.hero .btn-pink{left:175px;top:354px;width:148px;height:37px}

/* about */
.about{top:623px;left:0;width:1200px;height:477px;background:#e9e0d9}
.about-photo{left:569px;top:0;width:631px;height:477px;background:#eadfd6}
.about-card{left:188px;top:584px;width:380px;height:516px;background:var(--pink);color:var(--white)}
.about-card .hi{left:32px;top:50px;font-family:'Great Vibes',cursive;font-size:80px;line-height:1}
.about-card h2{left:32px;top:172px;font-size:33px;font-weight:700}
.about-card p{left:32px;top:234px;width:322px;font-size:13px;line-height:27px;font-weight:400;color:#fbe9e7}
.btn-outline-w{left:207px;top:431px;width:148px;height:38px;border:2px solid var(--white);border-radius:20px;
  font-size:10px;font-weight:700;display:flex;align-items:center;justify-content:center;gap:12px}

/* quote */
.quote{top:1100px;left:0;width:1200px;height:365px;background:var(--blush)}
.quote svg{left:0;top:0}
.quote blockquote{left:310px;top:96px;width:580px;text-align:center;font-style:italic;font-weight:300;font-size:18px;line-height:27px}
.quote .name{left:0;width:1200px;top:228px;text-align:center;font-size:28px;color:var(--teal-text);font-weight:400}
.quote .role{left:0;width:1200px;top:268px;text-align:center;font-size:13px;font-style:italic}
.quote .tag{left:0;width:1200px;top:289px;text-align:center;font-size:10px;font-style:italic}

/* spiritual */
.spirit{top:1465px;left:0;width:1200px;height:506px;background:var(--white)}
.spirit h3{left:173px;top:96px;font-size:22px;font-weight:400;line-height:28px}
.spirit p{left:173px;top:176px;width:252px;font-size:12.3px;line-height:27px;color:var(--grey);font-weight:300}
.player{left:173px;top:384px;width:257px;height:14px;display:flex;align-items:center;gap:6px;font-size:6px;color:var(--grey)}
.player .play{width:13px;height:12px;background:var(--ink)}
.player .bar{flex:1;height:3px;background:#bdbdbd;border-radius:2px}
.spirit .back{left:479px;top:65px;width:395px;height:258px;background:var(--teal-light)}
.spirit .photo{left:515px;top:102px;width:516px;height:330px;background:linear-gradient(180deg,#8a8f98,#d9a27a)}

/* posts */
.posts{top:1971px;left:0;width:1200px;height:608px;background:var(--mist)}
.section-title{left:0;width:1200px;text-align:center;font-size:22px;font-weight:400}
.posts .section-title{top:57px}
.post{top:140px;width:250px;height:420px}
.post .date{top:0;left:-3px;font-size:10px;font-weight:700;color:var(--teal-text)}
.post .img{top:19px;left:0;width:240px;height:201px}
.post h4{top:226px;left:0;width:215px;font-size:13.5px;font-weight:500;line-height:23px}
.post p{top:274px;left:-2px;width:225px;font-size:10.5px;line-height:18px;color:var(--grey);font-weight:300}
.post .more{top:338px;left:221px;width:20px;height:20px;background:var(--pink);color:var(--white);font-size:12px;display:flex;align-items:center;justify-content:center}

/* cta */
.cta{top:2579px;left:0;width:1200px;height:157px;background:var(--teal);color:var(--white)}
.cta h3{left:0;width:1200px;top:36px;text-align:center;font-size:22px;font-weight:700}
.cta a{left:534px;top:91px;width:139px;height:37px;border:2px solid var(--white);border-radius:20px;font-size:12px;display:flex;align-items:center;justify-content:center;gap:10px}

/* testimonials */
.testi{top:2736px;left:0;width:1200px;height:565px;background:var(--mist)}
.testi .section-title{top:58px}
.testi .intro{left:0;width:1200px;top:117px;text-align:center;font-size:13px;color:#555;font-weight:300}
.card{width:274px;background:var(--white);border-radius:10px}
.card p{position:absolute;left:20px;top:32px;width:234px;text-align:center;font-size:12.5px;line-height:18px;font-style:italic;font-weight:300;color:#555}
.badge{width:36px;height:36px;border-radius:50%;color:var(--white);font-family:Georgia,serif;font-size:30px;font-weight:700;display:flex;align-items:center;justify-content:center;line-height:1;padding-top:12px}
.avatar{width:74px;height:74px;border-radius:50%;background:#b9a697}
.person{width:274px;text-align:center;font-size:13px;text-transform:uppercase;letter-spacing:.3px}

/* newsletter */
.news{top:3301px;left:0;width:1200px;height:217px;background:var(--teal);color:var(--white)}
.news h3{left:0;width:1200px;top:38px;text-align:center;font-size:20px;font-weight:300;letter-spacing:.5px}
.field{top:99px;height:37px;background:var(--white);color:#aaa;font-size:12px;padding:0 13px;display:flex;align-items:center}
.submit{top:98px;left:903px;width:132px;height:38px;background:var(--pink);font-size:13px;font-weight:600;display:flex;align-items:center;justify-content:center;letter-spacing:.5px}
.consent{left:162px;top:158px;font-size:10px;display:flex;align-items:center;gap:8px}
.consent span{width:12px;height:12px;background:var(--white);display:inline-block}

/* contact */
.contact{top:3518px;left:0;width:1200px;height:137px;background:var(--white)}
.icon{width:50px;height:50px;border-radius:50%;display:flex;align-items:center;justify-content:center}
.contact .txt{font-size:10.5px;line-height:18px}
.contact .phone{font-size:24px;font-weight:300}
.footnav{top:3655px;left:0;width:1200px;height:50px;border-top:1px solid #e6e6e6;border-bottom:1px solid #e6e6e6;display:flex;justify-content:center;align-items:center;gap:26px;font-size:9.5px;text-transform:uppercase}
.copy{left:162px;top:3720px;font-size:9px;color:#555}
</style>
</head>
<body>

<header class="topnav abs">
  <nav class="links abs">
    <a class="active" style="left:0">Home</a>
    <a style="left:58px">About</a>
    <a style="left:119px">Podcast</a>
    <a style="left:191px">Blog</a>
    <a style="left:246px">Contact</a>
  </nav>
  <div class="social abs" style="left:955px;top:24px">snapverra <span>chirpline</span> <span>boardlyn</span></div>
</header>

<section class="hero abs">
  <div class="hero-photo abs" role="img" aria-label="Photo: woman in a flowing pink dress dancing in a wheat field under a blue sky"></div>
  <h1 class="abs">Unfold the hidden bloom</h1>
  <p class="abs">Lorem ipsum dolor sit amet, consectetur<br>adipiscing elit. Integer sit amet accumsan mauris.</p>
  <a class="btn-pink abs">LEARN MORE
    <svg width="16" height="16" viewBox="0 0 16 16"><circle cx="8" cy="8" r="7" fill="none" stroke="#fff" stroke-width="1.6"/><path d="M4.5 8h6M8 5.3 10.7 8 8 10.7" fill="none" stroke="#fff" stroke-width="1.6"/></svg></a>
</section>

<section class="about abs">
  <div class="about-photo abs" role="img" aria-label="Photo: portrait of Lunet smiling, long dark wavy hair, white top"></div>
</section>
<div class="about-card abs">
  <div class="hi abs">Hi !</div>
  <h2 class="abs">I’M Lunet</h2>
  <p class="abs">Lorem ipsum dolor sit amet, consectetur adipiscing elit. Quisque sed massa augue. Aenean quis pretium nunc. Proin ac arcu quis sem rutrum semper in eget odio. Interdum et malesuada fames ac ante ipsum primis in faucibus. Duis eu ligula in augue condimentum viverra.</p>
  <a class="btn-outline-w abs">LEARN MORE
    <svg width="16" height="16" viewBox="0 0 16 16"><circle cx="8" cy="8" r="7" fill="none" stroke="#fff" stroke-width="1.6"/><path d="M4.5 8h6M8 5.3 10.7 8 8 10.7" fill="none" stroke="#fff" stroke-width="1.6"/></svg></a>
</div>

<section class="quote abs">
  <svg class="abs" width="1200" height="365" viewBox="0 0 1200 365">
    <path d="M310 66H245V244H456M745 244H949V66H881" fill="none" stroke="var(--pink-soft)" stroke-width="2"/>
  </svg>
  <blockquote class="abs">"Your life is like a blank canvas and only you have the power to transform it into masterpiece. Take a chance and unfold the hidden bloom"</blockquote>
  <div class="name abs">Lunet</div>
  <div class="role abs">Life Coach</div>
  <div class="tag abs">(Unfold the hidden bloom)</div>
</section>

<section class="spirit abs">
  <h3 class="abs">Let me help you start<br>living a spiritual life!</h3>
  <p class="abs">Lorem ipsum dolor sit amet, consectetur adipiscing elit. Quisque sed massa augue. Aenean quis pretium nunc. Proin ac arcu quis sem rutrum semper in eget odio. Interdum et malesuada fames ac ante ipsum primis in faucibus. Duis eu ligula in augue condimentum viverra.</p>
  <div class="player abs"><span class="play"></span><span>0:00</span><span class="bar"></span><span>3:24</span><span>◂)</span></div>
  <div class="back abs"></div>
  <div class="photo abs" role="img" aria-label="Photo: woman meditating on a cliff edge at sunset"></div>
</section>

<section class="posts abs">
  <h2 class="section-title abs">Recent Posts</h2>
  <article class="post abs" style="left:169px">
    <div class="date abs">Thursday May 9th, 2019</div>
    <div class="img abs" role="img" aria-label="Photo: smiling man at a desk holding a pen" style="background:#c9c3bd"></div>
    <h4 class="abs">Donec vestibulum luctus felis, sit amet tincidunt</h4>
    <p class="abs">Lorem ipsum dolor sit amet, consectetur adipiscing elit. Quisque et tristique urna. Nulla sodales cursus mi et tincidunt.</p>
    <a class="more abs">›</a>
  </article>
  <article class="post abs" style="left:479px">
    <div class="date abs">Thursday May 9th, 2019</div>
    <div class="img abs" role="img" aria-label="Photo: two men standing with arms crossed in an office" style="background:#9a9ea5"></div>
    <h4 class="abs">Donec vestibulum luctus felis, sit amet tincidunt</h4>
    <p class="abs">Lorem ipsum dolor sit amet, consectetur adipiscing elit. Quisque et tristique urna. Nulla sodales cursus mi et tincidunt.</p>
    <a class="more abs">›</a>
  </article>
  <article class="post abs" style="left:789px">
    <div class="date abs">Thursday May 9th, 2019</div>
    <div class="img abs" role="img" aria-label="Photo: blonde woman with crossed arms in an office" style="background:#b7b9bd"></div>
    <h4 class="abs">Donec vestibulum luctus felis, sit amet tincidunt</h4>
    <p class="abs">Lorem ipsum dolor sit amet, consectetur adipiscing elit. Quisque et tristique urna. Nulla sodales cursus mi et tincidunt.</p>
    <a class="more abs">›</a>
  </article>
</section>

<section class="cta abs">
  <h3 class="abs">Feel spiritually connected every day!</h3>
  <a class="abs">Get Started
    <svg width="22" height="10" viewBox="0 0 22 10"><path d="M0 5h20M16 1l4 4-4 4" fill="none" stroke="#fff" stroke-width="1.3"/></svg></a>
</section>

<section class="testi abs">
  <h2 class="section-title abs">Testimonials</h2>
  <p class="intro abs">Donec vestibulum luctus felis, sit amet tincidunt lorem tincidunt a.</p>

  <div class="card abs" style="left:162px;top:208px;height:191px"><p>Lorem ipsum dolor sit amet, consectetur adipiscing elit. In iaculis, dolor sit amet tristique ornare, elit dolor maximus diam, ut hendrerit eros massa posuere velit.</p></div>
  <div class="badge abs" style="left:280px;top:190px;background:var(--teal)">”</div>
  <div class="avatar abs" role="img" aria-label="Photo: client portrait" style="left:261px;top:365px"></div>
  <div class="person abs" style="left:162px;top:456px">Theo Marchant</div>

  <div class="card abs" style="left:462px;top:208px;height:210px"><p>Lorem ipsum dolor sit amet, consectetur adipiscing elit. In iaculis, dolor sit amet tristique ornare, elit dolor maximus diam, ut hendrerit eros massa posuere velit. Lorem ipsum dolor sit amet, consectetur adipiscing elit.</p></div>
  <div class="badge abs" style="left:580px;top:190px;background:var(--pink)">”</div>
  <div class="avatar abs" role="img" aria-label="Photo: client portrait" style="left:561px;top:383px"></div>
  <div class="person abs" style="left:462px;top:469px">Rafe Colton</div>

  <div class="card abs" style="left:760px;top:208px;height:191px"><p>Lorem ipsum dolor sit amet, consectetur adipiscing elit. In iaculis, dolor sit amet tristique ornare, elit dolor maximus diam, ut hendrerit eros massa posuere velit.</p></div>
  <div class="badge abs" style="left:879px;top:190px;background:var(--teal)">”</div>
  <div class="avatar abs" role="img" aria-label="Photo: client portrait" style="left:860px;top:365px"></div>
  <div class="person abs" style="left:760px;top:456px">Rafe Colton</div>
</section>

<section class="news abs">
  <h3 class="abs">Signup For Our Newsletter</h3>
  <div class="field abs" style="left:162px;width:222px">First Name</div>
  <div class="field abs" style="left:409px;width:223px">Last Name</div>
  <div class="field abs" style="left:655px;width:224px">Email</div>
  <div class="submit abs">SUBMIT</div>
  <div class="consent abs"><span></span>Please see the privacy policy of the Unfold the hidden bloom.</div>
</section>

<section class="contact abs">
  <div class="icon abs" style="left:160px;top:43px;background:var(--teal)">
    <svg width="18" height="22" viewBox="0 0 18 22"><path d="M9 1a7 7 0 0 0-7 7c0 5 7 13 7 13s7-8 7-13a7 7 0 0 0-7-7z" fill="#fff"/><circle cx="9" cy="8" r="2.6" fill="var(--teal)"/></svg></div>
  <div class="txt abs" style="left:229px;top:38px"><span style="color:var(--teal)">Lunet</span><br>USA - LOS ANGELES,<br>418 Linden Row, Harbor Point,<br>CA 90021</div>
  <div class="icon abs" style="left:473px;top:43px;background:var(--pink)">
    <svg width="20" height="15" viewBox="0 0 20 15"><rect x="1" y="1" width="18" height="13" rx="2" fill="#fff"/><path d="M1.5 2 10 8.5 18.5 2" fill="none" stroke="var(--pink)" stroke-width="1.5"/></svg></div>
  <div class="txt abs" style="left:543px;top:60px">info@unfoldthehiddenbloom.com</div>
  <div class="icon abs" style="left:769px;top:43px;background:var(--teal)">
    <svg width="18" height="18" viewBox="0 0 18 18"><path d="M4 1l3 4-2 2c1 2 3 4 5 5l2-2 4 3-2 3C8 16 2 10 1 3z" fill="#fff"/></svg></div>
  <div class="phone abs" style="left:840px;top:51px">04 12 36 58 70</div>
</section>

<nav class="footnav abs">
  <a>Home</a><a>About</a><a>Podcast</a><a>Blog</a><a>Contact</a>
</nav>
<div class="copy abs">Copyright 2019 unfoldthehiddenbloom.com All Righs Reserved.</div>
<div class="social abs" style="left:955px;top:3719px">snapverra <span>chirpline</span> <span>boardlyn</span></div>

</body>
</html>
```